Layout for site fence advertising - length approx. 250 cm x 125 cm

The advertising will later be printed on a PVC film and used for events or on sports fields.

Main services :
Your regional contact at
Real estate and business financing
independent insurance advice

```html
<!DOCTYPE html>
<html lang="de">
<head>
<meta charset="utf-8">
<title>Halden Beratung GmbH – Bauzaunbanner</title>
<link rel="stylesheet" href="https://fonts.googleapis.com/css2?family=Kumbh+Sans:wght@600&family=Quicksand:wght@700&display=swap">
<style>
  :root {
    --brand-blue: #1a56c0;
    --band-blue: #0e0fc4;
    --slate: #666666;
    --paper: #ffffff;
    --edge: #111111;
  }
  * { margin: 0; padding: 0; box-sizing: border-box; }
  html, body { width: 1200px; height: 600px; overflow: hidden; background: var(--paper); }
  .banner {
    position: relative;
    width: 1200px;
    height: 600px;
    background: var(--paper);
    border: 1px solid var(--edge);
    overflow: hidden;
  }
  .brand-mark {
    position: absolute;
    left: 46px;
    top: 53px;
    width: 304px;
    height: 304px;
  }
  .divider {
    position: absolute;
    left: 378px;
    top: 50px;
    width: 9px;
    height: 308px;
    background: var(--slate);
  }
  .company-name {
    position: absolute;
    left: 409px;
    top: 130px;
    font-family: "Quicksand", sans-serif;
    font-weight: 700;
    font-size: 60px;
    line-height: 1;
    color: var(--brand-blue);
    white-space: nowrap;
  }
  .company-name .legal-form { font-size: 42px; margin-left: 10px; }
  .tagline {
    position: absolute;
    left: 409px;
    top: 212px;
    font-family: "Quicksand", sans-serif;
    font-weight: 700;
    font-size: 42px;
    line-height: 1;
    color: var(--slate);
    white-space: nowrap;
  }
  .services-band {
    position: absolute;
    left: 0;
    top: 402px;
    width: 100%;
    height: 198px;
    background: var(--band-blue);
  }
  .services-rule {
    position: absolute;
    left: 380px;
    top: 24px;
    width: 8px;
    height: 157px;
    background: var(--paper);
  }
  .services {
    position: absolute;
    left: 411px;
    top: 22px;
    font-family: "Kumbh Sans", sans-serif;
    font-weight: 600;
    font-size: 29px;
    line-height: 43px;
    color: var(--paper);
    list-style: none;
  }
  .services .service-gap { margin-top: 41px; }
</style>
</head>
<body>
  <main class="banner">
    <svg class="brand-mark" viewBox="0 0 304 304" aria-hidden="true">
      <circle cx="152" cy="152" r="144" fill="none" stroke="var(--brand-blue)" stroke-width="12"/>
    </svg>
    <div class="divider"></div>
    <h1 class="company-name">Halden Beratung<span class="legal-form">GmbH</span></h1>
    <p class="tagline">Finanzieren, Versichern, Vorsorgen</p>

    <section class="services-band">
      <div class="services-rule"></div>
      <ul class="services">
        <li>Your regional contact at real estate<br>and business financing</li>
        <li class="service-gap">Independent insurance advice</li>
      </ul>
    </section>
  </main>
</body>
</html>
```